Make it cool to work near where you are...

Calling all creatives - create the ultimate cool card for people who want to cut their commute.

Here at TilloPod we've got what can best be described as an Marlin pass for desks - and we want to brighten up the wallets of our most loyal users.

So, pitch us your ideas and you might see your design on cards being flashed across the country - and we've thrown in a bit of cash too.

Do see our brief card guidelines - with a couple of past examples thrown in.

Industry/Entity Type

Cash

```html
<!DOCTYPE html>
<html lang="en">
<head>
<meta charset="utf-8">
<title>TilloPod Membership Cards</title>
<link rel="stylesheet" href="https://fonts.googleapis.com/css2?family=Open+Sans:wght@400;700&display=swap">
<style>
  :root {
    --page: #ffffff;
    --maze-black: #0d0d0d;
    --maze-white: #f4f4f4;
    --accent-pink: #ec1e79;
    --band: #333333;
    --strip: rgba(200, 200, 200, 0.9);
    --strip-text: #1e1e1e;
    --cheese: #efac2f;
    --cheese-light: #f9d46e;
    --white: #ffffff;
  }
  html, body {
    margin: 0;
    padding: 0;
    width: 849px;
    height: 1200px;
    overflow: hidden;
    background: var(--page);
    font-family: "Open Sans", Arial, sans-serif;
  }
  .sheet {
    position: relative;
    width: 849px;
    height: 1200px;
  }
  .card {
    position: absolute;
    left: 250px;
    width: 348px;
    height: 217px;
    border-radius: 12px;
    overflow: hidden;
    background: var(--maze-black);
  }
  .card--front { top: 307px; }
  .card--back { top: 683px; }
  .card__maze {
    position: absolute;
    inset: 0;
    background: linear-gradient(135deg,
      var(--maze-black) 0%,
      var(--maze-white) 22%,
      var(--maze-black) 42%,
      var(--maze-white) 62%,
      var(--maze-black) 80%,
      var(--maze-white) 100%);
  }
  .card__maze--trail {
    background:
      radial-gradient(ellipse 70px 30px at 25px 70px, var(--accent-pink) 0%, rgba(236, 30, 121, 0.6) 50%, rgba(236, 30, 121, 0) 100%),
      linear-gradient(135deg,
        var(--maze-black) 0%,
        var(--maze-white) 22%,
        var(--maze-black) 42%,
        var(--maze-white) 62%,
        var(--maze-black) 80%,
        var(--maze-white) 100%);
  }
  .card__cheese {
    position: absolute;
    left: 67px;
    top: 71px;
    width: 50px;
    height: 42px;
    border-radius: 14px 18px 6px 6px;
    background: linear-gradient(160deg, var(--cheese-light), var(--cheese));
  }
  .card__number-strip {
    position: absolute;
    left: 0;
    top: 139px;
    width: 100%;
    height: 18px;
    background: var(--strip);
  }
  .card__number {
    position: absolute;
    left: 19px;
    top: 0;
    line-height: 18px;
    font-size: 14px;
    font-weight: 400;
    color: var(--strip-text);
  }
  .card__band {
    position: absolute;
    left: 0;
    bottom: 0;
    width: 100%;
    height: 37px;
    background: var(--band);
  }
  .card__web {
    position: absolute;
    left: 0;
    width: 100%;
    bottom: 11px;
    margin: 0;
    text-align: center;
    font-size: 11px;
    line-height: 14px;
    font-weight: 700;
    color: var(--white);
  }
  .card__brand {
    position: absolute;
    right: 22px;
    bottom: 26px;
    margin: 0;
    padding: 3px 6px;
    background: var(--maze-black);
    border-radius: 4px;
    font-size: 13px;
    line-height: 18px;
    font-weight: 700;
    color: var(--white);
  }
</style>
</head>
<body>
<main class="sheet">
  <section class="card card--front" aria-label="Card front">
    <div class="card__maze" role="img" aria-label="Bold black and white geometric maze pattern"></div>
    <div class="card__cheese" role="img" aria-label="Wedge of cheese illustration"></div>
    <div class="card__number-strip">
      <span class="card__number">0000 000 000 000</span>
    </div>
    <div class="card__band"></div>
    <p class="card__brand">TilloPod</p>
    <p class="card__web">www.tillopod.com</p>
  </section>

  <section class="card card--back" aria-label="Card back">
    <div class="card__maze card__maze--trail" role="img" aria-label="Bold black and white maze pattern with a pink path leading to the cheese"></div>
    <div class="card__cheese" role="img" aria-label="Wedge of cheese illustration"></div>
    <div class="card__band"></div>
    <p class="card__brand">TilloPod</p>
    <p class="card__web">www.tillopod.com</p>
  </section>
</main>
</body>
</html>
```